Business Card Design Project

Our logo/name is trademarked (since around 2000) and is owned by us. Logo originally designed in 1984 by my wife. Our logo needs freshening up while retaining its recognizability and trademark coverage. Our business cards, line card etc., web page home also need freshening, maybe as simple as inserting the updated logo, or completely redesigned.

Our logo represents "torque", which is defined as a force around an axis or "twist". Since 1949, we have been one of the world leaders in Norlane industrial clutches and brakes sales and service. We specialize in heavy duty applications such as stamping presses, steel mills, paper mills, drilling rigs etc. We are engineers as well as business people. Our customers are maintenance supervisors, plant engineers, small business owners. Our "color" has been reflex blue For more background, our website is www.brindlemark-co.com
Updates

I have posted a correct scan of the card/logo front and some previous versions of our logo.  (For now skip the back.)

As my brief said, we are after refreshing the logo and our cards/literature but the logo and card first.

Project Deadline Extended
Reason: I had trouble getting my existing logo scanned. should be up now.

Hopefully, the third try loading my existing logo and card worked!  The "City" banner had been on the0 bottom of the card.

Alt. A:  leave cities off
Alt B.  Instead of the cities, take a look at our web site home page or second page showing the world map and see if the world (as a territory which we do ship worldwide) could be worked in or highlight the back of the
 card with lines and the world? 

Future project will be line card redesign and web site
with separate project budget etc.www.brindlemark-co.com

Project Deadline Extended
Reason: My business partner was out of town last week and I wanted a couple days for his input. Thank you for your patience

Thank you all for your input! Dale Hurst

Target Market(s)

factory maintenance managers, plant engineers, small business owners

Industry/Entity Type

Small Business

Requirements
Must have
• clear development of existing trademarked logo

```html
<!DOCTYPE html>
<html lang="en">
<head>
<meta charset="utf-8">
<title>Brindlemark Business Card</title>
<link href="https://fonts.googleapis.com/css2?family=Open+Sans:ital,wght@0,400;0,700;0,800;1,700&display=swap" rel="stylesheet">
<style>
  :root {
    --backdrop: #3a3a3a;
    --card-white: #ffffff;
    --card-black: #000000;
    --accent-blue: #4aa6dc;
    --title-blue: #3b8fd0;
    --ink: #111111;
    --contact-text: #e6e6e6;
  }
  html, body {
    margin: 0;
    padding: 0;
    width: 1200px;
    height: 800px;
    overflow: hidden;
    background: var(--backdrop);
    font-family: "Open Sans", Arial, sans-serif;
  }
  .card {
    position: absolute;
    left: 75px;
    top: 100px;
    width: 1050px;
    height: 600px;
    background: var(--card-white);
    overflow: hidden;
  }
  .card-bands {
    position: absolute;
    inset: 0;
    width: 1050px;
    height: 600px;
  }
  .brand {
    position: absolute;
    right: 70px;
    top: 95px;
    display: flex;
    align-items: center;
    gap: 22px;
  }
  .brand-name {
    font-weight: 800;
    font-size: 56px;
    letter-spacing: 1px;
    color: var(--ink);
  }
  .brand-mark {
    width: 110px;
    height: 110px;
    border-radius: 50%;
    background: var(--title-blue);
  }
  .holder {
    position: absolute;
    left: 56px;
    top: 338px;
  }
  .holder-name {
    margin: 0;
    font-weight: 700;
    font-style: italic;
    font-size: 42px;
    line-height: 1.2;
    color: var(--card-white);
  }
  .holder-title {
    margin: 0;
    font-weight: 400;
    font-style: italic;
    font-size: 31px;
    line-height: 1.2;
    color: var(--title-blue);
  }
  .contact {
    position: absolute;
    right: 75px;
    top: 372px;
    margin: 0;
    text-align: right;
    font-style: normal;
    font-size: 25px;
    line-height: 34px;
    color: var(--contact-text);
  }
  .website {
    position: absolute;
    left: 56px;
    top: 540px;
    font-size: 24px;
    color: var(--card-white);
  }
</style>
</head>
<body>
  <article class="card">
    <svg class="card-bands" viewBox="0 0 1050 600" aria-hidden="true">
      <polygon points="0,322 1050,298 1050,600 0,600" fill="var(--accent-blue)"/>
      <polygon points="0,330 1050,332 1050,600 0,600" fill="var(--card-black)"/>
    </svg>

    <div class="brand">
      <span class="brand-name">BRINDLEMARK</span>
      <span class="brand-mark" aria-hidden="true"></span>
    </div>

    <div class="holder">
      <p class="holder-name">Dale Hurst</p>
      <p class="holder-title">CEO</p>
    </div>

    <address class="contact">
      2280 N. Harlow Ridge Suite 140<br>
      Carverton, MI 48390-1174<br>
      (555) 410-2280<br>
      Fax (555) 410-2291<br>
      Parts Hotline (800) 555-0147<br>
      dhurst@brindlemark-co.com
    </address>

    <div class="website">www.brindlemark-co.com</div>
  </article>
</body>
</html>
```